Need new sign at entrance for new fruit and vegetable wholesaler in market. Main vegetables sold are
Broccoli , Cauliflower , cabbage , capsicum , tomatoes , lettuce .
Business name is Tenby Crop
I have included examples of other designs and a sketch of suggested layout.
Business

```html
<!DOCTYPE html>
<html lang="en">
<head>
<meta charset="utf-8">
<title>Tenby Crop – Entrance Sign</title>
<link rel="stylesheet" href="https://fonts.googleapis.com/css2?family=Russo+One&family=Arimo:wght@700&display=swap">
<style>
  :root {
    --leaf-green: #abcd37;
    --leaf-green-dark: #8fb226;
    --white: #ffffff;
    --ink: #111511;
    --phone-fill: #b7d435;
    --tile-shadow: #3c3f3a;
    --swoosh-line: #e6efd2;
  }
  html, body {
    margin: 0;
    padding: 0;
    overflow: hidden;
    background: #ffffff;
  }
  .sign {
    position: relative;
    width: 1200px;
    height: 330px;
    background: var(--leaf-green);
    overflow: hidden;
    font-family: "Russo One", sans-serif;
  }
  .business-name {
    position: absolute;
    left: 30px;
    top: 18px;
    margin: 0;
    font-family: "Russo One", sans-serif;
    font-weight: 400;
    font-size: 122px;
    line-height: 1;
    letter-spacing: 2px;
    color: var(--white);
    white-space: nowrap;
  }
  .location {
    position: absolute;
    left: 963px;
    top: 16px;
    margin: 0;
    font-family: "Arimo", sans-serif;
    font-weight: 700;
    font-size: 29px;
    line-height: 39px;
    letter-spacing: 1px;
    color: var(--white);
  }
  .swoosh {
    position: absolute;
    left: 0;
    top: 160px;
    width: 420px;
    height: 170px;
  }
  .contact {
    position: absolute;
    left: 28px;
    top: 212px;
    width: 310px;
    text-align: center;
    font-family: "Russo One", sans-serif;
    color: var(--phone-fill);
    -webkit-text-stroke: 1.6px var(--ink);
    paint-order: stroke fill;
    letter-spacing: 2px;
  }
  .contact-label {
    display: block;
    font-size: 38px;
    line-height: 44px;
  }
  .contact-number {
    display: block;
    font-size: 42px;
    line-height: 52px;
    margin-top: 2px;
  }
  .produce-row {
    position: absolute;
    left: 403px;
    top: 199px;
    display: flex;
    gap: 15px;
    margin: 0;
    padding: 0;
    list-style: none;
  }
  .produce-tile {
    width: 118px;
    height: 118px;
    border-radius: 8px;
    background: var(--white);
    box-shadow: -4px -4px 0 var(--tile-shadow);
    display: flex;
    align-items: center;
    justify-content: center;
  }
  .produce-photo {
    width: 104px;
    height: 88px;
    border-radius: 40%;
  }
  .photo-tomato { background: radial-gradient(circle at 45% 45%, #f05a3c, #c81e10); }
  .photo-broccoli { background: radial-gradient(circle at 50% 40%, #6f9a3a, #2f5a18); }
  .photo-cabbage { background: radial-gradient(circle at 50% 45%, #d9ecab, #8dbb4e); }
  .photo-cauliflower { background: radial-gradient(circle at 50% 45%, #fbf8ee, #d9d4bd); }
  .photo-lettuce { background: radial-gradient(circle at 50% 45%, #8fd04a, #3f8f1e); }
  .photo-capsicum { background: linear-gradient(90deg, #c0161b 0%, #e2b21a 45%, #2f7a1c 100%); }
</style>
</head>
<body>
<main class="sign">
  <h1 class="business-name">Tenby Crop</h1>

  <p class="location">STAND 214<br>C SHED</p>

  <svg class="swoosh" viewBox="0 0 420 170" aria-hidden="true">
    <defs>
      <linearGradient id="swooshFade" x1="0" y1="0" x2="1" y2="0">
        <stop offset="0" stop-color="#f2f6e8"/>
        <stop offset="1" stop-color="#ffffff"/>
      </linearGradient>
    </defs>
    <path d="M0 18 C120 10 260 30 340 90 C375 116 395 145 405 170 L0 170 Z" fill="url(#swooshFade)"/>
    <path d="M0 30 C60 60 110 110 130 170" stroke="var(--swoosh-line)" stroke-width="3" fill="none"/>
    <path d="M0 60 C40 90 70 130 80 170" stroke="var(--swoosh-line)" stroke-width="3" fill="none"/>
    <path d="M0 95 C20 120 35 145 40 170" stroke="var(--swoosh-line)" stroke-width="3" fill="none"/>
    <path d="M20 15 C110 50 180 110 200 170" stroke="var(--swoosh-line)" stroke-width="2" fill="none"/>
  </svg>

  <p class="contact">
    <span class="contact-label">Phone/Fax</span>
    <span class="contact-number">02 5550 1947</span>
  </p>

  <ul class="produce-row">
    <li class="produce-tile"><div class="produce-photo photo-tomato" role="img" aria-label="Photo of fresh whole and halved tomatoes"></div></li>
    <li class="produce-tile"><div class="produce-photo photo-broccoli" role="img" aria-label="Photo of broccoli florets"></div></li>
    <li class="produce-tile"><div class="produce-photo photo-cabbage" role="img" aria-label="Photo of a green cabbage cut open"></div></li>
    <li class="produce-tile"><div class="produce-photo photo-cauliflower" role="img" aria-label="Photo of a cauliflower head"></div></li>
    <li class="produce-tile"><div class="produce-photo photo-lettuce" role="img" aria-label="Photo of green leafy lettuce"></div></li>
    <li class="produce-tile"><div class="produce-photo photo-capsicum" role="img" aria-label="Photo of red, yellow and green capsicums"></div></li>
  </ul>
</main>
</body>
</html>
```